FOLI PACK FOR STICKS

Design the packaging for salted sticks (weight 400g) reference to the logo TOVEN (in attached).
Color packaging- look forward to suggestions.
Package with window.
Hi, we need only graphic conception without texts on back side.

Please find Logo TOVEN and the grid of packaging - attached
Updates

we need only graphic conception without texts on back side. Added Saturday, November 08, 2014

Target Market(s)

typical salted snack for everyone (adults and children included)

Font styles to use
Sans Serif

Requirements
Should not have
• - religion and politic signs…
• - toys and childdraws
• - monsters, devils and demons etc.

```html
<!DOCTYPE html>
<html lang="en">
<head>
<meta charset="utf-8">
<title>TOVEN Pretzel Sticks – Front Pack</title>
<link href="https://fonts.googleapis.com/css2?family=Archivo+Black&family=Roboto+Condensed:wght@400;700&family=Patrick+Hand&display=swap" rel="stylesheet">
<style>
  :root {
    --pack-red: #e3141d;
    --pack-red-dark: #b80e16;
    --pack-yellow: #d9b21c;
    --pack-blue: #1d3e94;
    --pack-blue-dark: #142e75;
    --title-blue: #1b3d9c;
    --brand-brown: #6b4418;
    --badge-green: #16924a;
    --snack-light: #d49a52;
    --snack-dark: #8e5a24;
    --ink: #111111;
    --white: #ffffff;
    --page: #ffffff;
  }
  html, body {
    margin: 0;
    padding: 0;
    width: 900px;
    height: 1200px;
    overflow: hidden;
    background: var(--page);
  }
  .canvas {
    position: relative;
    width: 900px;
    height: 1200px;
  }
  .pack {
    position: absolute;
    left: 0;
    top: 0;
  }
  .claim {
    font-family: "Roboto Condensed", Arial, sans-serif;
    font-weight: 700;
    font-size: 20px;
    fill: var(--white);
  }
  .brand-name {
    font-family: "Roboto Condensed", Arial, sans-serif;
    font-weight: 700;
    font-size: 50px;
    fill: var(--brand-brown);
    letter-spacing: 1px;
  }
  .product-title {
    font-family: "Archivo Black", "Arial Black", sans-serif;
    fill: var(--white);
    stroke: var(--title-blue);
    paint-order: stroke fill;
    stroke-linejoin: round;
  }
  .product-title--small { font-size: 52px; stroke-width: 9px; }
  .product-title--large { font-size: 100px; stroke-width: 12px; }
  .flavour {
    font-family: "Patrick Hand", cursive;
    font-size: 28px;
    fill: var(--ink);
    letter-spacing: 1px;
  }
  .badge-number {
    font-family: "Roboto Condensed", Arial, sans-serif;
    font-weight: 700;
    font-size: 34px;
    fill: var(--white);
  }
  .badge-label {
    font-family: "Roboto Condensed", Arial, sans-serif;
    font-weight: 700;
    font-size: 19px;
    fill: var(--white);
  }
  .gluten-text {
    font-family: "Roboto Condensed", Arial, sans-serif;
    font-weight: 700;
    fill: var(--white);
  }
  .net-weight {
    font-family: "Roboto Condensed", Arial, sans-serif;
    font-weight: 400;
    font-size: 14.5px;
    fill: var(--white);
  }
</style>
</head>
<body>
<main class="canvas">
  <svg class="pack" width="900" height="1200" viewBox="0 0 900 1200" xmlns="http://www.w3.org/2000/svg">
    <defs>
      <pattern id="teeth-top" width="8" height="10" patternUnits="userSpaceOnUse" x="173" y="110">
        <path d="M0 10 L4 2 L8 10 Z" fill="var(--pack-red)"/>
      </pattern>
      <pattern id="teeth-bottom" width="8" height="10" patternUnits="userSpaceOnUse" x="173" y="956">
        <path d="M0 0 L4 8 L8 0 Z" fill="var(--pack-blue)"/>
      </pattern>
      <pattern id="crimp-red" width="5" height="10" patternUnits="userSpaceOnUse">
        <rect width="5" height="10" fill="var(--pack-red)"/>
        <rect width="1.5" height="10" fill="var(--pack-red-dark)"/>
      </pattern>
      <pattern id="crimp-blue" width="5" height="10" patternUnits="userSpaceOnUse">
        <rect width="5" height="10" fill="var(--pack-blue)"/>
        <rect width="1.5" height="10" fill="var(--pack-blue-dark)"/>
      </pattern>
      <linearGradient id="snack-fill" x1="0" y1="0" x2="1" y2="0">
        <stop offset="0" stop-color="var(--snack-dark)"/>
        <stop offset="0.5" stop-color="var(--snack-light)"/>
        <stop offset="1" stop-color="var(--snack-dark)"/>
      </linearGradient>
    </defs>

    <!-- top seal -->
    <rect class="seal-teeth" x="173" y="110" width="587" height="10" fill="url(#teeth-top)"/>
    <rect class="seal-crimp" x="173" y="120" width="587" height="30" fill="url(#crimp-red)"/>

    <!-- upper red field -->
    <rect class="field-red" x="173" y="150" width="587" height="330" fill="var(--pack-red)"/>

    <!-- product window -->
    <polygon class="product-window" role="img" aria-label="Window showing lightly salted pretzel sticks"
             points="173,620 760,560 760,790 173,850" fill="url(#snack-fill)"/>

    <!-- lower blue field -->
    <polygon class="field-blue" points="173,850 760,785 760,925 173,925" fill="var(--pack-blue)"/>
    <rect class="seal-crimp" x="173" y="925" width="587" height="31" fill="url(#crimp-blue)"/>
    <rect class="seal-teeth" x="173" y="956" width="587" height="10" fill="url(#teeth-bottom)"/>

    <!-- title band -->
    <polygon class="title-band-edge" points="173,458 630,372 632,360 760,348 760,597 173,658" fill="var(--white)"/>
    <polygon class="title-band" points="173,467 640,380 642,368 760,357 760,588 173,648" fill="var(--pack-yellow)"/>

    <!-- claim -->
    <text class="claim" x="466" y="194" text-anchor="middle">70% Less Fat and 40% More Protein</text>

    <!-- brand -->
    <rect class="brand-plate" x="362" y="262" width="204" height="84" rx="12" fill="var(--white)"/>
    <circle class="brand-dot" cx="464" cy="250" r="14" fill="var(--white)"/>
    <text class="brand-name" x="464" y="324" text-anchor="middle">TOVEN</text>

    <!-- product name -->
    <g transform="rotate(-7 470 470)">
      <text class="product-title product-title--small" x="490" y="450" text-anchor="middle">PRETZEL</text>
      <text class="product-title product-title--large" x="470" y="550" text-anchor="middle">STICKS</text>
      <text class="flavour" x="462" y="600" text-anchor="middle">Lightly Salted</text>
    </g>

    <!-- calorie badge -->
    <circle class="calorie-badge-ring" cx="303" cy="650" r="52" fill="var(--white)"/>
    <circle class="calorie-badge" cx="303" cy="650" r="46" fill="var(--badge-green)"/>
    <text class="badge-number" x="303" y="652" text-anchor="middle">100</text>
    <text class="badge-label" x="303" y="678" text-anchor="middle">Calories</text>

    <!-- gluten free mark -->
    <rect class="gluten-mark" x="595" y="772" width="74" height="76" rx="5" fill="var(--ink)"/>
    <text class="gluten-text" x="632" y="800" text-anchor="middle" font-size="19">Gluten</text>
    <text class="gluten-text" x="632" y="836" text-anchor="middle" font-size="28">FREE</text>

    <!-- net weight -->
    <text class="net-weight" x="466" y="890" text-anchor="middle">8-1.76 OZ. (50G) SNACK PACKS • NET WT.14.1 OZ. (400G)</text>
  </svg>
</main>
</body>
</html>
```